Paying WELL above market rates to find the very best Powerpoint Designer for keynote presentations..

Large cap tech company on the west coast is looking to bring a fresh and innovative new look to a series of keynote presentations. There will be 4 x 30 slide decks over the next 3 months. We are the whale customer you want to land!...We are prepared to pay WELL about market rates to attract the very best designers to work on our project.

Attached are the slides I would like repainted... we did these internally, but I need them to be redesigned....

Target Market(s)

Enterprise Corporate

Industry/Entity Type

It Company

```html
<!DOCTYPE html>
<html lang="en">
<head>
<meta charset="utf-8">
<title>Business Profile</title>
<link rel="stylesheet" href="https://fonts.googleapis.com/css2?family=Roboto:wght@400;500&family=Arimo&display=swap">
<style>
  :root {
    --bg: #f8f9fd;
    --blue: #2a6bb4;
    --navy: #2a4a8d;
    --charcoal: #333333;
    --indigo: #4a4a96;
    --violet: #453f7c;
    --title-grey: #a2a2a6;
    --sub-grey: #acacb0;
    --body-grey: #8a8a8e;
    --accent: #2a6bb4;
  }
  * { margin: 0; padding: 0; box-sizing: border-box; }
  html, body { width: 1200px; height: 900px; overflow: hidden; }
  body { background: var(--bg); font-family: "Roboto", Arial, sans-serif; position: relative; }

  .top-bar { position: absolute; top: 0; left: 0; width: 1200px; height: 20px; display: flex; }
  .top-bar span { height: 100%; }
  .top-bar .seg-1 { width: 240px; background: var(--blue); }
  .top-bar .seg-2 { width: 241px; background: var(--navy); }
  .top-bar .seg-3 { width: 240px; background: var(--charcoal); }
  .top-bar .seg-4 { width: 479px; background: var(--indigo); }

  .slide-title { position: absolute; left: 64px; top: 74px; font-size: 38px; font-weight: 500; color: var(--title-grey); }
  .slide-subtext { position: absolute; left: 64px; top: 152px; width: 1090px; font-size: 18.5px; line-height: 33px; color: var(--sub-grey); }
  .section-title { position: absolute; left: 71px; top: 273px; font-size: 23px; font-weight: 500; color: var(--accent); }

  .process { position: absolute; left: 0; top: 0; }

  .step-text { position: absolute; top: 487px; font-family: "Arimo", Arial, sans-serif; font-size: 17.5px; line-height: 24.5px; color: var(--body-grey); }
  .col-1 { left: 85px; } .col-2 { left: 297px; } .col-3 { left: 501px; } .col-4 { left: 703px; } .col-5 { left: 910px; }

  .footer-bar { position: absolute; left: 0; bottom: 0; width: 1200px; height: 36px; background: var(--charcoal); }
</style>
</head>
<body>
  <div class="top-bar"><span class="seg-1"></span><span class="seg-2"></span><span class="seg-3"></span><span class="seg-4"></span></div>

  <h1 class="slide-title">Project Title Here</h1>
  <p class="slide-subtext">Subtext here Subtext here Subtext here Subtext here Subtext here Subtext here Subtext here Subtext here Subtext here Sub-text here Subtext here Subtext here Subtext here Subtext here Subtext here Subtext here</p>
  <h2 class="section-title">Business Profile Title Here</h2>

  <svg class="process" width="1200" height="900" viewBox="0 0 1200 900" aria-hidden="true">
    <defs>
      <g id="bulb" fill="none" stroke="#fff" stroke-width="2.2" stroke-linecap="round" stroke-linejoin="round">
        <path d="M -8 12 C -8 4 -17 -1 -17 -12 A 17 17 0 1 1 17 -12 C 17 -1 8 4 8 12 Z"/>
        <path d="M -4 12 L -4 -4 M 4 12 L 4 -4"/>
        <path d="M -4 -4 C -9 -8 -9 -14 -4 -12 C -1 -11 0 -7 0 -4 C 0 -7 1 -11 4 -12 C 9 -14 9 -8 4 -4"/>
        <path d="M -9 16 H 9 M -9 21 H 9 M -7 26 H 7 M -4 30 H 4"/>
      </g>
    </defs>
    <g stroke="#fff" stroke-width="3" stroke-linejoin="miter">
      <polygon fill="var(--blue)" points="64,320 282,320 307,392 282,464 64,464"/>
      <polygon fill="var(--navy)" points="279,320 485,320 510,392 485,464 279,464 304,392"/>
      <polygon fill="var(--charcoal)" points="483,320 686,320 711,392 686,464 483,464 508,392"/>
      <polygon fill="var(--indigo)" points="685,320 892,320 917,392 892,464 685,464 710,392"/>
      <polygon fill="var(--violet)" points="888,320 1094,320 1119,392 1094,464 888,464 913,392"/>
    </g>
    <use href="#bulb" x="182" y="393"/>
    <use href="#bulb" x="404" y="393"/>
    <use href="#bulb" x="588" y="393"/>
    <use href="#bulb" x="801" y="393"/>
    <use href="#bulb" x="996" y="393"/>
  </svg>

  <p class="step-text col-1">Lorem ipsum dolor sit<br>Lorem ipsum dolor sit<br>Lorem ipsum dolor sit<br>Lorem ipsum dolor sit<br>Lorem ipsum dolor sit<br>Lorem ipsum dolor sit<br>Lorem ipsum dolor sit<br>Lorem ipsum dolor sit</p>
  <p class="step-text col-2">Lorem ipsum dolor sit<br>Lorem ipsum dolor sit<br>Lorem ipsum dolor sit<br>Lorem ipsum dolor sit<br>Lorem ipsum dolor sit<br>Lorem ipsum dolor sit<br>Lorem ipsum dolor sit<br>Lorem ipsum dolor sit</p>
  <p class="step-text col-3">Lorem ipsum dolor sit<br>Lorem ipsum dolor sit<br>Lorem ipsum dolor sit<br>Lorem ipsum dolor sit<br>Lorem ipsum dolor sit<br>Lorem ipsum dolor sit<br>Lorem ipsum dolor sit<br>Lorem ipsum dolor sit</p>
  <p class="step-text col-4">Lorem ipsum dolor sit<br>Lorem ipsum dolor sit<br>Lorem ipsum dolor sit<br>Lorem ipsum dolor sit<br>Lorem ipsum dolor sit<br>Lorem ipsum dolor sit<br>Lorem ipsum dolor sit<br>Lorem ipsum dolor sit</p>
  <p class="step-text col-5">Lorem ipsum dolor sit<br>Lorem ipsum dolor sit<br>Lorem ipsum dolor sit<br>Lorem ipsum dolor sit<br>Lorem ipsum dolor sit<br>Lorem ipsum dolor sit<br>Lorem ipsum dolor sit<br>Lorem ipsum dolor sit</p>

  <div class="footer-bar"></div>
</body>
</html>
```